TobinFarral.com - emergency management consultant, tv news commentator, public speaker

We need a website built for my company based in the SF Bay area. We have a logo design and now are looking for a new website. Our current site is tobinfarral.com needs a major overhaul. Our new business line and focus will be as a public speaker. We would like to utilize our tv news commentator segments for the site.
Updates

We have been in negotiations with company for work outside the US. I am the only employee of this new company and work negotiations have overshadowed this component of the new business.

We have narrowed the field down to a few design by 2 designers. I had previously asked the designers to incorporate the "copy content" we uploaded to this site, they have not done so yet.

We are completing the last of the revisions

Target Market(s)

Keynote address for conventions, etc

Coding

Coded - Design and coding required

Number of Pages Required

5+ page

Colors

Designer to choose colors to be used in the design.

Requirements
Must have
• video capability and the standard website pages: about, contact, services, etc
Nice to have
• ?
Should not have
• ?

```html
<!DOCTYPE html>
<html lang="en">
<head>
<meta charset="utf-8">
<title>Tobin Farral — Emergency Management Expert</title>
<link rel="stylesheet" href="https://fonts.googleapis.com/css2?family=Cormorant+Garamond:ital,wght@0,400;0,500;0,600;1,400;1,500&family=Raleway:wght@400;500;600;700&display=swap">
<style>
:root{
  --crimson:#8e1c2c;
  --crimson-dark:#731523;
  --navy:#0b0d30;
  --navy-mid:#1a1f4a;
  --ink:#1d1d24;
  --body:#5b5d66;
  --mist:#f3f4f9;
  --line:#e3e4ec;
  --white:#ffffff;
}
*{box-sizing:border-box;margin:0;padding:0}
html,body{width:1200px;height:4390px;overflow:hidden}
body{font-family:"Raleway",Arial,sans-serif;color:var(--body);background:var(--white);position:relative}
.btn{position:absolute;display:flex;align-items:center;justify-content:center;gap:10px;font-family:"Raleway",Arial,sans-serif;font-weight:700;letter-spacing:2px;text-transform:uppercase;font-size:12px;color:var(--white);background:var(--crimson)}
.btn-ghost{background:var(--white);color:var(--crimson);box-shadow:0 6px 18px rgba(20,20,50,.12)}

/* hero */
.hero{position:absolute;left:0;top:0;width:1200px;height:717px;background:radial-gradient(ellipse at 45% 65%,#2a2440 0%,#131537 45%,var(--navy) 100%)}
.hero-photo{position:absolute;inset:0;background:radial-gradient(circle at 42% 70%,rgba(120,90,110,.35),rgba(0,0,0,0) 40%)}
.nav{position:absolute;left:0;top:0;width:1200px;height:73px;background:rgba(6,8,30,.75)}
.brand{position:absolute;left:255px;top:18px;font-family:"Cormorant Garamond",Georgia,serif;font-size:30px;font-weight:500;color:#c9a6ad;letter-spacing:1px}
.nav-link{position:absolute;top:27px;font-size:14px;font-weight:500;color:var(--white)}
.hero h1{position:absolute;left:117px;top:175px;width:950px;font-family:"Cormorant Garamond",Georgia,serif;font-weight:500;font-size:60px;line-height:64px;color:var(--white)}
.hero-roles{position:absolute;left:117px;top:315px;font-size:24px;font-weight:500;color:var(--white)}
.hero-copy{position:absolute;left:117px;top:395px;width:900px;font-size:15px;line-height:24px;color:#d6d7e3}

/* about */
.about{position:absolute;left:0;top:717px;width:1200px;height:694px;background:var(--white)}
.portrait{position:absolute;left:600px;top:9px;width:480px;height:685px;background:linear-gradient(180deg,#d9dade 0%,#c7c8cc 55%,#2a2d3a 100%)}
.about h2{position:absolute;left:117px;top:120px;font-family:"Cormorant Garamond",Georgia,serif;font-weight:500;font-size:50px;color:var(--ink)}
.about .titles{position:absolute;left:117px;top:197px;width:380px;font-family:"Cormorant Garamond",Georgia,serif;font-weight:600;font-size:31px;line-height:41px;color:var(--crimson)}
.about p{position:absolute;left:117px;top:330px;width:370px;font-size:13px;line-height:22px}

/* specialties */
.expertise{position:absolute;left:0;top:1411px;width:1200px;height:591px;background:var(--mist)}
.expertise h2{position:absolute;left:117px;top:94px;width:420px;font-family:"Cormorant Garamond",Georgia,serif;font-weight:500;font-size:35px;line-height:50px;color:var(--ink)}
.spec{position:absolute;width:210px}
.spec svg{display:block;width:66px;height:66px}
.spec h3{margin-top:24px;font-size:13px;font-weight:700;color:var(--ink)}
.spec p{margin-top:10px;font-size:12px;line-height:20px}
.divider{position:absolute;left:620px;top:586px;width:460px;border-top:2px dashed var(--line)}

/* video */
.media{position:absolute;left:0;top:2002px;width:1200px;height:407px;background:linear-gradient(180deg,var(--white) 0%,var(--white) 75%,var(--mist) 75%)}
.video-still{position:absolute;left:44px;top:0;width:553px;height:316px;background:linear-gradient(115deg,#cfd8e6 0%,#8797ad 35%,#3b3d45 70%,#2a2b31 100%)}
.play{position:absolute}
.gallery-link{position:absolute;left:597px;top:94px;width:483px;height:111px;background:var(--crimson);display:flex;align-items:center;padding-left:55px;font-family:"Cormorant Garamond",Georgia,serif;font-size:24px;color:var(--white)}
.video-caption{position:absolute;left:112px;top:322px;font-size:11px;color:var(--body)}

/* testimonial */
.testimonial{position:absolute;left:0;top:2409px;width:1200px;height:629px}
.quote-panel{position:absolute;left:0;top:0;width:600px;height:629px;background:var(--crimson)}
.quote-panel .label{position:absolute;left:32px;top:118px;font-family:"Cormorant Garamond",Georgia,serif;font-style:italic;font-size:20px;color:var(--white)}
.quote-panel blockquote{position:absolute;left:32px;top:188px;width:520px;font-family:"Cormorant Garamond",Georgia,serif;font-style:italic;font-size:20px;line-height:38px;color:var(--white)}
.event-photo{position:absolute;left:600px;top:0;width:600px;height:629px;background:linear-gradient(160deg,#b9c3cf 0%,#8c8a84 35%,#3a3736 70%,#22222a 100%)}

/* featured */
.featured-title{position:absolute;left:0;top:3128px;width:1200px;text-align:center;font-family:"Cormorant Garamond",Georgia,serif;font-weight:500;font-size:37px;color:var(--crimson)}
.featured-band{position:absolute;left:117px;top:3202px;width:963px;height:100px;background:var(--crimson);display:flex;align-items:center;justify-content:space-around;padding:0 20px}
.featured-band span{font-family:"Raleway",Arial,sans-serif;font-weight:600;font-size:17px;color:var(--white);letter-spacing:1px;text-transform:uppercase;display:flex;align-items:center;gap:8px}
.featured-band i{display:inline-block;width:12px;height:12px;border-radius:50%;background:var(--white)}

/* go-to expert */
.goto h2{position:absolute;left:117px;top:3372px;width:420px;font-family:"Cormorant Garamond",Georgia,serif;font-weight:500;font-size:35px;line-height:48px;color:var(--ink)}
.goto p{position:absolute;left:117px;top:3508px;width:390px;font-size:12.5px;line-height:22px}
.news-still{position:absolute;left:623px;top:3372px;width:457px;height:258px;background:linear-gradient(180deg,#3f6fae 0%,#2a4f86 55%,#1b2c55 100%)}

/* contact */
.contact{position:absolute;left:0;top:3746px;width:1200px;height:644px;background:linear-gradient(180deg,var(--white) 0%,var(--mist) 100%)}
.contact h2{position:absolute;left:117px;top:80px;font-family:"Cormorant Garamond",Georgia,serif;font-weight:600;font-size:44px;color:var(--crimson)}
.contact .intro{position:absolute;left:117px;top:172px;width:400px;font-size:12.5px;line-height:22px}
.info{position:absolute;left:117px;display:flex;gap:20px}
.info .dot{width:28px;height:28px;border-radius:50%;background:var(--crimson);display:flex;align-items:center;justify-content:center}
.info b{display:block;font-size:13px;font-weight:600;color:var(--ink)}
.info span{display:block;margin-top:8px;font-size:11.5px}
.form-card{position:absolute;left:623px;top:88px;width:457px;height:445px;background:var(--white);box-shadow:0 10px 40px rgba(20,20,60,.08);padding:22px 40px}
.field{height:42px;background:var(--mist);margin-bottom:18px;font-size:11.5px;display:flex;align-items:center;padding-left:14px;color:var(--body)}
.field.area{height:130px;align-items:flex-start;padding-top:14px}
.submit{position:absolute;right:42px;bottom:28px;width:86px;height:26px;background:var(--crimson);color:var(--white);font-size:11px;font-weight:700;letter-spacing:2px;display:flex;align-items:center;justify-content:center}
.social{position:absolute;top:574px;width:40px;height:40px;background:var(--crimson);display:flex;align-items:center;justify-content:center}
.social i{width:10px;height:10px;border-radius:50%;background:var(--white)}
</style>
</head>
<body>

<section class="hero">
  <div class="hero-photo" role="img" aria-label="Dim conference hall with a speaker's microphone in soft focus"></div>
  <nav class="nav">
    <div class="brand">Tobin Farral</div>
    <a class="nav-link" style="left:623px">Home</a>
    <a class="nav-link" style="left:793px">About</a>
    <a class="nav-link" style="left:962px">Contact</a>
  </nav>
  <h1>Presidential-Appointed Emergency Management Expert</h1>
  <div class="hero-roles">Expert | TV Commentator | Public Speaker | Panelist | Consultant</div>
  <p class="hero-copy">Preparedness work begins long before disaster strikes. Plans are tested, teams are trained and communities learn how to respond together. With decades of service in public safety, every engagement blends practical field lessons with clear strategy that leaders can use right away. Agencies, boards and conventions rely on this calm guidance when the stakes are highest and time is short, turning complex risk into steps people remember.</p>
  <a class="btn" style="left:117px;top:582px;width:141px;height:41px;letter-spacing:0;text-transform:none;font-size:15px;font-weight:500">Get in Touch</a>
</section>

<section class="about">
  <div class="portrait" role="img" aria-label="Studio portrait of Tobin Farral in a dark suit and red tie"></div>
  <h2>Tobin Farral</h2>
  <div class="titles">Emergency Management Consultant | TV News Commentator | Public Speaker</div>
  <p>Tobin has guided cities, counties and agencies through fires, floods and quakes. His keynote talks share lessons from the front lines and help audiences build stronger plans for the next emergency.</p>
  <a class="btn" style="left:117px;top:495px;width:196px;height:41px">Get in Touch
    <svg width="8" height="10" viewBox="0 0 8 10"><path d="M2 1l4 4-4 4" fill="none" stroke="#fff" stroke-width="1.6"/></svg></a>
  <a class="btn btn-ghost" style="left:117px;top:547px;width:199px;height:41px;font-size:11px;letter-spacing:1.5px">Call: (415) 555-0148
    <svg width="8" height="10" viewBox="0 0 8 10"><path d="M2 1l4 4-4 4" fill="none" stroke="#8e1c2c" stroke-width="1.6"/></svg></a>
</section>

<section class="expertise">
  <h2>A Presidential Appointee with 25 Years of Expertise on Emergency Management</h2>
  <a class="btn" style="left:117px;top:281px;width:156px;height:50px">Get in Touch</a>

  <div class="spec" style="left:623px;top:90px">
    <svg viewBox="0 0 66 66" fill="none" stroke="#8e1c2c" stroke-width="2"><circle cx="33" cy="33" r="22"/><path d="M20 20c6 4 4 10 10 12s3 10 8 12M40 14c-2 6 4 8 9 9"/></svg>
    <h3>Specialty 1</h3>
    <p>Regional disaster planning for cities, counties and public safety agencies.</p>
  </div>
  <div class="spec" style="left:878px;top:90px">
    <svg viewBox="0 0 66 66" fill="none" stroke="#8e1c2c" stroke-width="2"><path d="M14 28h10l20-10v30L24 38H14z"/><path d="M20 38l4 12h6l-3-12M50 26l6-3M50 33h7M50 40l6 3"/></svg>
    <h3>Specialty 2</h3>
    <p>Crisis communication and media briefings during active incidents.</p>
  </div>
  <div class="spec" style="left:623px;top:345px">
    <svg viewBox="0 0 66 66" fill="none" stroke="#8e1c2c" stroke-width="2"><rect x="12" y="26" width="30" height="20"/><circle cx="20" cy="18" r="7"/><circle cx="36" cy="18" r="7"/><path d="M42 32l12-6v20l-12-6M22 46l-4 10M32 46l4 10"/></svg>
    <h3>Specialty 3</h3>
    <p>On-air analysis for news teams covering fires, storms and quakes.</p>
  </div>
  <div class="spec" style="left:878px;top:345px">
    <svg viewBox="0 0 66 66" fill="none" stroke="#8e1c2c" stroke-width="2"><rect x="12" y="12" width="42" height="42"/><rect x="18" y="18" width="30" height="30"/><path d="M24 33l7 7 14-14"/></svg>
    <h3>Specialty 4</h3>
    <p>Keynote talks and panels for conventions and leadership events.</p>
  </div>
  <div class="divider"></div>
</section>

<section class="media">
  <div class="video-still" role="img" aria-label="Close-up of hands holding a smartphone, video thumbnail"></div>
  <svg class="play" width="80" height="80" viewBox="0 0 80 80" style="left:236px;top:98px"><circle cx="40" cy="40" r="36" fill="rgba(255,255,255,.15)" stroke="#fff" stroke-width="4"/><path d="M32 25l22 15-22 15z" fill="#fff"/></svg>
  <a class="gallery-link">View Gallery &amp; Videos &nbsp;›</a>
  <div class="video-caption">Video</div>
</section>

<section class="testimonial">
  <div class="quote-panel">
    <div class="label">Testimonial</div>
    <blockquote>“Tobin kept our whole county calm and focused. His plan was clear, his updates were honest, and his talk to our staff still shapes how we train. We could not have asked for a better guide when everything was at stake.”</blockquote>
  </div>
  <div class="event-photo" role="img" aria-label="Tobin Farral speaking at a microphone among officials at a disaster site"></div>
</section>

<div class="featured-title">Featured By:</div>
<div class="featured-band">
  <span><i></i>Harbor</span>
  <span>Bayline</span>
  <span>Summit</span>
  <span>Crestline</span>
  <span>Meridian</span>
  <span>Solace</span>
</div>

<section class="goto">
  <h2>The Go-To Expert When Emergencies Happen</h2>
  <p>When a crisis breaks, newsrooms call Tobin for clear and steady analysis. His segments explain what is happening, what comes next and how viewers can stay safe, making complex response efforts easy for every audience to follow.</p>
  <a class="btn" style="left:117px;top:3668px;width:146px;height:50px">Learn More
    <svg width="8" height="10" viewBox="0 0 8 10"><path d="M2 1l4 4-4 4" fill="none" stroke="#fff" stroke-width="1.6"/></svg></a>
  <div class="news-still" role="img" aria-label="Television news segment with Tobin Farral as on-screen commentator"></div>
</section>

<section class="contact">
  <h2>Get In Touch</h2>
  <p class="intro">Book Tobin for a keynote, panel or media segment. Share a few details about your event and he will reply within two business days.</p>
  <div class="info" style="top:285px">
    <div class="dot"><svg width="12" height="14" viewBox="0 0 12 14"><path d="M6 13S1 8 1 5a5 5 0 0110 0c0 3-5 8-5 8z" fill="#fff"/><circle cx="6" cy="5" r="1.8" fill="#8e1c2c"/></svg></div>
    <div><b>Location</b><span>San Jose, California</span></div>
  </div>
  <div class="info" style="top:361px">
    <div class="dot"><svg width="12" height="12" viewBox="0 0 12 12"><path d="M2 1h3l1 3-2 1c1 2 2 3 4 4l1-2 3 1v3c-6 0-10-4-10-10z" fill="#fff"/></svg></div>
    <div><b>Phone</b><span>(415) 555-0148</span></div>
  </div>
  <div class="info" style="top:437px">
    <div class="dot"><svg width="12" height="10" viewBox="0 0 12 10"><rect x="0.5" y="0.5" width="11" height="9" fill="#fff"/><path d="M1 1l5 4 5-4" fill="none" stroke="#8e1c2c"/></svg></div>
    <div><b>Email</b><span>info@tobinfarral.com</span></div>
  </div>

  <form class="form-card">
    <div class="field">Name</div>
    <div class="field">Email Address</div>
    <div class="field">Phone Number</div>
    <div class="field area">Message</div>
    <div class="submit">SUBMIT</div>
  </form>

  <a class="social" style="left:764px"><i></i></a>
  <a class="social" style="left:829px"><i></i></a>
  <a class="social" style="left:896px"><i></i></a>
</section>

</body>
</html>
```